Online-Marketing Material für Beraternetzwerk
Zielgruppe
Ich habe ein Beraternetzwerk im deutschen Gesundheitswesen gegründet, gleichzeitig einen gemeinnützigen Verein, habe zwei webseiten www.kv-pflegeberatung-demo.de + www.kv-pflegefreunde-demo.de, Logo, Briefpapier etc. sind vorhanden. Hauptfarbe GmbH RGB 185/87/120 Hex#B95778, Verein RGB 226/125/119 Hex#E27D77. Die Organisationen sind grundsätzlich getrennt, aber es gibt eine Zusammenarbeit und Partner meines Netzwerkes sind auch Fördermitglieder im Verein
Aufgabenstellung
Die beiden Firmenfarben müssen verwendet werden, für die GmbH hauptsächlich die eigene, die 2. Farbe darf mit verwendet werden. Es darf insgesamt feminin wirken, aber nicht verspielt oder gar niedlich. Ich bin Business-Frau;-). Als Schrift habe ich mich auf Avenir next konzentriert, die Agentur hat auch Alternate Gothic auf den Webseiten verwendet. Jetzt benötige ich für eine Veranstaltungsreihe die Ausarbeitung von LinkedIn, Facebook/Insta, Einladung per Brevo und E-Mail Grafiken. Es sind immer Veranstaltungen, zu denen ich einlade und in denen meine Geschäftspartner ihre Expertise gegenüber Kunden darstellen. Die Veranstaltungen sind als Duo zu sehen 1. Präsenz in München, 2. als Online Meeting ein paar Tage später. Die Location wird das Hotel Marwin, direkt am Brunnenhofplatz in München sein. Start der Präsenzveranstaltung 11:00, anschließend Mittagessen. Als Titel für die Veranstaltungen sehe ich 'KlinikForum' vor, es wird jeweils noch ein inhaltliches Thema wie z.B. 'Unternehmenskauf/-verkauf' ergänzt. Erster Termin ist vss. am 15. September 2023. Anbei auch ein paar erste Entwürfe 'meiner' Agentur nebst Feedback von mir. Ich glaube inzwischen nicht, dass hier etwas vernünftiges produziert wird, deshalb mein Versuch auf diesem Weg. Weitere Zusammenarbeit dann herzlich gerne

```html
<!DOCTYPE html>
<html lang="de">
<head>
<meta charset="utf-8">
<title>KlinikForum – Unternehmenskauf/-verkauf</title>
<link rel="stylesheet" href="https://fonts.googleapis.com/css2?family=Nunito+Sans:wght@200;300;400;600;700;800;900&display=swap">
<style>
  :root {
    --rose: #C85680;
    --rose-mid: #D27585;
    --peach: #D9957F;
    --plum: #9E4262;
    --white: #FFFFFF;
  }
  html, body {
    margin: 0;
    padding: 0;
    width: 1200px;
    height: 1200px;
    overflow: hidden;
  }
  .poster {
    position: relative;
    width: 1200px;
    height: 1200px;
    overflow: hidden;
    color: var(--white);
    font-family: "Nunito Sans", sans-serif;
    background:
      radial-gradient(ellipse 700px 600px at 1050px 80px, rgba(222,160,130,0.75), rgba(222,160,130,0) 70%),
      linear-gradient(100deg, var(--rose) 0%, var(--rose-mid) 50%, var(--peach) 100%);
  }
  .shapes {
    position: absolute;
    inset: 0;
  }
  .brand {
    position: absolute;
    left: 72px;
    top: 36px;
    display: flex;
    align-items: center;
    gap: 22px;
  }
  .brand-dot {
    width: 90px;
    height: 90px;
    border-radius: 50%;
    background: var(--white);
  }
  .brand-name {
    font-weight: 700;
    font-size: 38px;
    line-height: 1.05;
  }
  .title-light {
    position: absolute;
    left: 64px;
    top: 148px;
    font-weight: 200;
    font-size: 262px;
    line-height: 1;
    letter-spacing: 6px;
  }
  .title-bold {
    position: absolute;
    left: 70px;
    top: 400px;
    font-weight: 900;
    font-size: 212px;
    line-height: 1;
    letter-spacing: -2px;
  }
  .topic {
    position: absolute;
    left: 110px;
    top: 648px;
    font-weight: 800;
    font-size: 42px;
  }
  .venue {
    position: absolute;
    left: 96px;
    top: 778px;
    width: 470px;
    text-align: center;
  }
  .venue-label {
    font-weight: 800;
    font-size: 41px;
    line-height: 1.1;
  }
  .venue-time {
    font-weight: 900;
    font-size: 80px;
    line-height: 1.05;
  }
  .online {
    position: absolute;
    left: 148px;
    top: 938px;
    font-weight: 400;
    font-size: 30px;
    line-height: 40px;
  }
  .date {
    position: absolute;
    left: 890px;
    top: 500px;
    width: 310px;
    text-align: center;
  }
  .date-day {
    font-weight: 900;
    font-size: 182px;
    line-height: 1;
    letter-spacing: -3px;
  }
  .date-month {
    font-weight: 300;
    font-size: 58px;
    line-height: 1.05;
  }
  .date-year {
    font-weight: 900;
    font-size: 122px;
    line-height: 1;
  }
  .signup {
    position: absolute;
    left: 56px;
    top: 1072px;
    font-size: 18px;
    line-height: 1.2;
    text-align: center;
  }
  .signup-note { font-weight: 400; }
  .signup-cta { font-weight: 800; }
  .contact {
    position: absolute;
    left: 64px;
    top: 1156px;
    font-weight: 400;
    font-size: 26px;
    white-space: nowrap;
  }
</style>
</head>
<body>
<main class="poster">
  <svg class="shapes" width="1200" height="1200" viewBox="0 0 1200 1200" aria-hidden="true">
    <polygon class="date-panel" points="864,431 1200,494 1200,922 864,844" fill="#9E4262"/>
    <polygon class="online-band" points="89,929 650,929 594,987 56,987" fill="#9E4262"/>
  </svg>

  <header class="brand">
    <div class="brand-dot"></div>
    <div class="brand-name">KV Pflegeberatung<br>GmbH</div>
  </header>

  <h1 class="title-light" style="margin:0">KLINIK</h1>
  <div class="title-bold">FORUM</div>

  <p class="topic" style="margin:0">“Unternehmenskauf/-verkauf”</p>

  <div class="venue">
    <div class="venue-label">Präsenzveranstaltung</div>
    <div class="venue-time">11:00 Uhr</div>
  </div>

  <div class="online">Online am x.xx. 17:00 Uhr</div>

  <div class="date">
    <div class="date-day">15.</div>
    <div class="date-month">September</div>
    <div class="date-year">2023</div>
  </div>

  <div class="signup">
    <div class="signup-note">Begrenzte Teilnehmerzahl</div>
    <div class="signup-cta">Bitte anmelden unter:</div>
  </div>

  <div class="contact">petra.wolff@kv-pflegeberatung-demo.de • kv-pflegeberatung-demo.de</div>
</main>
</body>
</html>
```